Boilerplate Management Organization Chart

"Our Management Approach is a deliberate step-by-step process and supports our Technical Approach detailed in proposal submission. The Management Approach covers all the human capital aspects for executing a contract—from contract award through to sustainment and/or transition of the contract to another company. It includes how we organize, hire, staff, train, and account for our contract employees—as well as their complete personal life-cycle management within the company."

We need this management approach to depict an amazing management process that demonstrates best practices of the project management body of knowledge. We need this vector image to be applicable to any proposal without making references to any other proposals. Generic names but using strong business language.
Updates

Thanks for all designs submitted thus far. Some have stuck to the original type of chart. We would like to see a completely different way to show the same information. It has to be able to be recognized and deciphered very quickly by people who might not necessarily want to look at it. It must draw them in and make it incredibly easy to distinguish a management approach that looks fresh, infallible, and easily implemented.

Target Market(s)

Federal space, Government organizations looking for procedural efficiencies,

Industry/Entity Type

Management

Requirements
Must have
• Must not take up more than 1/3 to 1/2 of printable page and be clear.
Should not have
• Not too much color, but should stick to some color palette of some interest.

```html
<!DOCTYPE html>
<html lang="en">
<head>
<meta charset="utf-8">
<title>Management Approach Process</title>
<link rel="stylesheet" href="https://fonts.googleapis.com/css2?family=Montserrat:ital,wght@0,700;1,700&display=swap">
<style>
  :root {
    --page: #fdfcf9;
    --warm-fill: #fde9d4;
    --warm-ring: #fccdb0;
    --warm-wedge: #fdebd3;
    --sand-fill: #f0e8d6;
    --sand-ring: #c6c1ae;
    --sand-wedge: #f1e9d8;
    --heading: #5f5f5f;
    --label: #1e1e1e;
    --pointer: #5f5f5f;
  }
  html, body {
    margin: 0;
    padding: 0;
    width: 1200px;
    height: 1000px;
    overflow: hidden;
    background: var(--page);
  }
  .process-chart {
    display: block;
    width: 1200px;
    height: 1000px;
  }
  .section-title {
    font-family: "Montserrat", sans-serif;
    font-weight: 700;
    font-style: italic;
    font-size: 33px;
    fill: var(--heading);
    letter-spacing: -0.5px;
  }
  .step-label {
    font-family: "Montserrat", sans-serif;
    font-weight: 700;
    font-size: 16.5px;
    fill: var(--label);
    text-anchor: middle;
  }
  .warm .step-disc { fill: var(--warm-fill); }
  .warm .step-ring { stroke: var(--warm-ring); }
  .sand .step-disc { fill: var(--sand-fill); }
  .sand .step-ring { stroke: var(--sand-ring); }
  .step-ring { fill: none; stroke-width: 14; }
  .flow-arrow.warm-arrow { fill: var(--warm-ring); }
  .flow-arrow.sand-arrow { fill: var(--sand-ring); }
  .turn-arrow { fill: var(--pointer); }
  .wedge-warm { fill: var(--warm-wedge); }
  .band-warm { fill: var(--warm-ring); }
  .wedge-sand { fill: var(--sand-wedge); }
  .band-sand { fill: var(--sand-ring); }
</style>
</head>
<body>
<svg class="process-chart" viewBox="0 0 1200 1000" xmlns="http://www.w3.org/2000/svg" role="img" aria-label="Management approach process from responsibility fixed to sustainment and transition">

  <!-- Management approach header -->
  <g class="header-band">
    <polygon class="wedge-warm" points="163,130 1035,222 1035,224 163,224"/>
    <rect class="band-warm" x="163" y="224" width="872" height="12"/>
    <text class="section-title" x="173" y="218">MANAGEMENT APPROACH</text>
  </g>

  <!-- Top row steps -->
  <g class="step warm">
    <circle class="step-disc" cx="255" cy="367" r="87"/>
    <circle class="step-ring" cx="255" cy="367" r="94" stroke-dasharray="305 1000" transform="rotate(25 255 367)"/>
    <text class="step-label" x="255" y="364">RESPONSABILITY</text>
    <text class="step-label" x="255" y="388">FIXED</text>
  </g>
  <polygon class="flow-arrow warm-arrow" points="350,340 385,367 350,395"/>

  <g class="step warm">
    <circle class="step-disc" cx="490" cy="367" r="87"/>
    <circle class="step-ring" cx="490" cy="367" r="94" stroke-dasharray="303 1000" transform="rotate(150 490 367)"/>
    <text class="step-label" x="490" y="353">MANAGEMENT</text>
    <text class="step-label" x="490" y="376">&amp;</text>
    <text class="step-label" x="490" y="400">OVERSIGHT</text>
  </g>
  <polygon class="flow-arrow warm-arrow" points="583,340 618,367 583,395"/>

  <g class="step warm">
    <circle class="step-disc" cx="722" cy="367" r="87"/>
    <circle class="step-ring" cx="722" cy="367" r="94" stroke-dasharray="289 1000" transform="rotate(31 722 367)"/>
    <text class="step-label" x="722" y="364">MANNING</text>
    <text class="step-label" x="722" y="388">THE TEAM</text>
  </g>
  <polygon class="flow-arrow warm-arrow" points="817,340 852,367 817,395"/>

  <g class="step warm">
    <circle class="step-disc" cx="958" cy="367" r="87"/>
    <circle class="step-ring" cx="958" cy="367" r="94" stroke-dasharray="307 1000" transform="rotate(148 958 367)"/>
    <text class="step-label" x="958" y="376">TRAINING</text>
  </g>

  <polygon class="turn-arrow" points="927,483 983,483 955,517"/>

  <!-- Bottom row steps -->
  <g class="step sand">
    <circle class="step-disc" cx="955" cy="638" r="87"/>
    <circle class="step-ring" cx="955" cy="638" r="94" stroke-dasharray="341 1000" transform="rotate(191 955 638)"/>
    <text class="step-label" x="947" y="636">PROFESSIONAL</text>
    <text class="step-label" x="947" y="660">DEVELOPMENT</text>
  </g>
  <polygon class="flow-arrow sand-arrow" points="850,612 815,638 850,665"/>

  <g class="step sand">
    <circle class="step-disc" cx="722" cy="638" r="87"/>
    <circle class="step-ring" cx="722" cy="638" r="94" stroke-dasharray="315 1000" transform="rotate(-35 722 638)"/>
    <text class="step-label" x="708" y="636">RETENTION /</text>
    <text class="step-label" x="708" y="660">QUALITY OF LIFE</text>
  </g>
  <polygon class="flow-arrow sand-arrow" points="617,612 582,638 617,665"/>

  <g class="step sand">
    <circle class="step-disc" cx="483" cy="638" r="87"/>
    <circle class="step-ring" cx="483" cy="638" r="94" stroke-dasharray="312 1000" transform="rotate(200 483 638)"/>
    <text class="step-label" x="462" y="644">BENEFITS</text>
  </g>
  <polygon class="flow-arrow sand-arrow" points="385,612 350,638 385,665"/>

  <g class="step sand">
    <circle class="step-disc" cx="250" cy="638" r="87"/>
    <circle class="step-ring" cx="250" cy="638" r="94" stroke-dasharray="356 1000" transform="rotate(-60 250 638)"/>
    <text class="step-label" x="236" y="636">SUSTAINMENT /</text>
    <text class="step-label" x="236" y="660">TRANSITION</text>
  </g>

  <!-- Program evaluation footer -->
  <g class="footer-band">
    <rect class="band-sand" x="165" y="763" width="872" height="13"/>
    <polygon class="wedge-sand" points="165,776 1037,776 1037,868"/>
    <text class="section-title" x="1025" y="808" text-anchor="end">PROGRAM EVALUATION</text>
  </g>
</svg>
</body>
</html>
```